modern, IT themed business card for IT accelerator

Design a business card for tech oriented business accelerator. Prevailing color shall be orange.
we are operating in emerging markets and our mission is to provide co-working space, mentorship/coaching and ultimately seed financing IT startups.
also, we are helping financed ITs in obtaining next round financing, and to this end we are meeting with non IT/finance people and investment professionals..
that means card shall be designed to "impress" not only IT people (mostly liberal) but finance (more conservative)

Industry/Entity Type

Investment

Contact Information for Business Card

Company Name: Pelor Founders Yard
Name: Temur Kobaladze
Position: Partner
Address: 14, N Abashidze St., Tbilisi 0162, Georgia
Tel: +995599438165
Email: t.kobaladze@pelorhub.ge
Website: www.pelorhub.ge

Font styles to use
Sans Serif

Requirements
Must have
• Attached are logos of the company (portrait & landscape) choose any
Nice to have
• industry is IT and finance (in fact, financing IT startups). therefore design might have IT theme (inspiration from web or software designs)

```html
<!DOCTYPE html>
<html lang="en">
<head>
<meta charset="utf-8">
<title>Pelor Founders Yard — Business Card</title>
<link rel="stylesheet" href="https://fonts.googleapis.com/css2?family=Barlow:wght@500&family=Roboto+Condensed:wght@400&family=Questrial&display=swap">
<style>
  :root {
    --backdrop: #8f8f8f;
    --card-white: #f7f7f7;
    --card-silver: #e2e2e2;
    --band-dark: #9a9a9a;
    --band-light: #eeeeee;
    --orange: #e8801f;
    --orange-light: #f08f2a;
    --orange-deep: #d8691a;
    --logo-grey: #7c7f84;
    --text-grey: #6f6f6f;
    --white: #ffffff;
  }
  * { box-sizing: border-box; margin: 0; padding: 0; }
  html, body {
    width: 1200px; height: 900px; overflow: hidden;
    background: var(--backdrop);
  }
  .card {
    position: absolute; left: 100px; top: 160px;
    width: 1000px; height: 580px;
    border-radius: 44px; overflow: hidden;
    background: var(--card-white);
    box-shadow: 0 10px 30px rgba(0,0,0,0.25);
  }
  .card__top {
    position: absolute; left: 0; top: 0; width: 100%; height: 300px;
    background: radial-gradient(ellipse at 35% 45%, var(--white) 0%, var(--card-white) 45%, var(--card-silver) 100%);
  }
  .card__band {
    position: absolute; left: 0; top: 300px; width: 100%; height: 10px;
    background: linear-gradient(90deg, var(--band-light) 0%, var(--band-dark) 35%, var(--band-light) 60%, var(--band-dark) 100%);
  }
  .card__bottom {
    position: absolute; left: 0; top: 310px; width: 100%; height: 270px;
    background: linear-gradient(120deg, var(--orange-deep) 0%, var(--orange) 35%, var(--orange-light) 60%, var(--orange-deep) 100%);
  }
  .brand {
    position: absolute; left: 70px; top: 70px;
    display: flex; align-items: center; gap: 34px;
  }
  .brand__mark {
    width: 150px; height: 150px; border-radius: 50%;
    background: var(--orange);
  }
  .brand__name {
    font-family: "Barlow", sans-serif; font-weight: 500;
    color: var(--logo-grey); line-height: 1;
  }
  .brand__name-main { display: block; font-size: 104px; letter-spacing: 2px; text-transform: uppercase; }
  .brand__name-sub { display: block; font-size: 38px; letter-spacing: 1px; margin-top: 8px; text-transform: uppercase; }
  .holder {
    position: absolute; right: 70px; top: 48px; text-align: right;
  }
  .holder__name {
    font-family: "Roboto Condensed", sans-serif; font-weight: 400;
    font-size: 36px; color: var(--orange);
  }
  .holder__role {
    font-family: "Roboto Condensed", sans-serif;
    font-size: 18px; color: var(--text-grey); margin-top: 4px;
  }
  .contacts {
    position: absolute; left: 60px; top: 365px; list-style: none;
    font-family: "Questrial", sans-serif; font-size: 27px; color: var(--white);
    line-height: 36px;
  }
  .contacts__item { display: flex; align-items: flex-start; gap: 10px; }
  .contacts__icon { width: 30px; height: 30px; margin-top: 3px; flex: none; }
  .contacts__text--indent { padding-left: 40px; }
</style>
</head>
<body>
  <div class="card">
    <div class="card__top" role="img" aria-label="Faint silver tech pattern of circuit rings and arrows"></div>
    <div class="card__band"></div>
    <div class="card__bottom" role="img" aria-label="Orange low-poly faceted background"></div>

    <div class="brand">
      <div class="brand__mark"></div>
      <div class="brand__name">
        <span class="brand__name-main">Pelor</span>
        <span class="brand__name-sub">Founders Yard</span>
      </div>
    </div>

    <div class="holder">
      <div class="holder__name">Temur Kobaladze</div>
      <div class="holder__role">Partner</div>
    </div>

    <ul class="contacts">
      <li class="contacts__item">
        <svg class="contacts__icon" viewBox="0 0 24 24" fill="#dcdcdc"><path d="M6.6 10.8a15.1 15.1 0 0 0 6.6 6.6l2.2-2.2c.3-.3.7-.4 1-.2 1.1.4 2.3.6 3.6.6.6 0 1 .4 1 1V20c0 .6-.4 1-1 1A17 17 0 0 1 3 4c0-.6.4-1 1-1h3.5c.6 0 1 .4 1 1 0 1.3.2 2.5.6 3.6.1.3 0 .7-.2 1z"/></svg>
        <span>+995599438165</span>
      </li>
      <li class="contacts__item">
        <svg class="contacts__icon" viewBox="0 0 24 24" fill="#dcdcdc"><path d="M2 5h20v14H2z"/><path d="M2 5l10 8 10-8" fill="none" stroke="#e8801f" stroke-width="1.6"/></svg>
        <span>t.kobaladze@pelorhub.ge</span>
      </li>
      <li class="contacts__item">
        <svg class="contacts__icon" viewBox="0 0 24 24" fill="none" stroke="#dcdcdc" stroke-width="1.8"><circle cx="12" cy="12" r="9.5"/><ellipse cx="12" cy="12" rx="4.5" ry="9.5"/><path d="M2.5 12h19M4 7h16M4 17h16"/></svg>
        <span>www.pelorhub.ge</span>
      </li>
      <li class="contacts__item">
        <svg class="contacts__icon" viewBox="0 0 24 24" fill="#dcdcdc"><path d="M12 3l10 9h-3v9h-5v-6h-4v6H5v-9H2z"/></svg>
        <span>14, N Abashidze St.,</span>
      </li>
      <li class="contacts__item contacts__text--indent">
        <span>Tbilisi 0162, Georgia</span>
      </li>
    </ul>
  </div>
</body>
</html>
```